Norwell Asset Partners, LLC

I need a new business card desperately.

Please update my business card. I am looking for a professional modern classy design like the Brisket Holdings card in the attachments.

Industry/Entity Type

Investment

Contact Information for Business Card

Colors

Designer to choose colors to be used in the design.

```html
<!DOCTYPE html>
<html lang="en">
<head>
<meta charset="utf-8">
<title>Norwell Asset Partners — Business Card</title>
<link href="https://fonts.googleapis.com/css2?family=Lato:ital,wght@0,300;0,400;0,700;0,900;1,700&display=swap" rel="stylesheet">
<style>
  :root {
    --navy: #1c2c3a;
    --gold: #b07a2e;
    --card-top: #f3efeb;
    --card-bottom: #e9e1db;
    --backdrop: #cfc6bd;
    --ink: #1f2326;
  }
  * { box-sizing: border-box; margin: 0; padding: 0; }
  html, body { width: 1200px; height: 970px; overflow: hidden; }
  body {
    background: var(--backdrop);
    font-family: "Lato", sans-serif;
    color: var(--ink);
    position: relative;
  }
  .business-card {
    position: absolute;
    left: 80px; top: 188px;
    width: 1040px; height: 594px;
    background: linear-gradient(180deg, var(--card-top), var(--card-bottom));
    box-shadow: 0 18px 40px rgba(0,0,0,.18);
    overflow: hidden;
  }
  .holder { position: absolute; left: 57px; top: 58px; line-height: 1; }
  .holder-name { font-size: 31px; color: var(--navy); letter-spacing: -.3px; }
  .holder-name .first { font-weight: 900; }
  .holder-name .last { font-weight: 400; }
  .holder-role { font-size: 25px; font-weight: 300; color: var(--gold); margin-top: 2px; }
  .website {
    position: absolute; right: 55px; top: 64px;
    font-size: 23px; font-weight: 700; font-style: italic; color: var(--navy);
  }
  .website .domain { color: var(--gold); }
  .brand {
    position: absolute; left: 0; right: 0; top: 255px;
    display: flex; justify-content: center; align-items: center; gap: 18px;
  }
  .brand-mark { width: 34px; height: 34px; background: var(--navy); }
  .brand-name {
    font-size: 36px; font-weight: 700; letter-spacing: 3px;
    color: var(--navy); text-transform: uppercase;
  }
  .divider {
    position: absolute; left: 57px; right: 55px; top: 467px;
    height: 2px; background: var(--gold);
  }
  .contact-list {
    position: absolute; left: 57px; top: 488px;
    list-style: none; font-size: 25px; line-height: 33px; color: var(--ink);
  }
  .contact-list li { display: flex; align-items: center; gap: 10px; }
  .contact-icon { width: 28px; height: 28px; flex: none; }
  .address {
    position: absolute; right: 55px; top: 488px;
    font-size: 25px; line-height: 33px; text-align: right; color: var(--ink);
    font-style: normal;
  }
  .base-band {
    position: absolute; left: 0; right: 0; bottom: 0; height: 16px;
    background: var(--navy);
  }
</style>
</head>
<body>
  <section class="business-card">
    <div class="holder">
      <div class="holder-name"><span class="first">OWEN</span> <span class="last">HALE</span></div>
      <div class="holder-role">Owner</div>
    </div>

    <div class="website">www.<span class="domain">NORWELLASSET</span>.com</div>

    <div class="brand">
      <span class="brand-mark"></span>
      <span class="brand-name">Norwell Asset Partners, LLC</span>
    </div>

    <div class="divider"></div>

    <ul class="contact-list">
      <li>
        <svg class="contact-icon" viewBox="0 0 28 28" aria-hidden="true">
          <circle cx="14" cy="14" r="14" fill="var(--gold)"/>
          <rect x="9.5" y="6.5" width="9" height="15" rx="1.8" fill="none" stroke="#fff" stroke-width="1.8"/>
          <line x1="12.5" y1="18.5" x2="15.5" y2="18.5" stroke="#fff" stroke-width="1.6"/>
        </svg>
        (555) 284-6130
      </li>
      <li>
        <svg class="contact-icon" viewBox="0 0 28 28" aria-hidden="true">
          <circle cx="14" cy="14" r="14" fill="var(--gold)"/>
          <rect x="7" y="9" width="14" height="10" rx="1" fill="none" stroke="#fff" stroke-width="1.8"/>
          <polyline points="7.5,9.5 14,15 20.5,9.5" fill="none" stroke="#fff" stroke-width="1.6"/>
        </svg>
        owen@norwellasset.com
      </li>
    </ul>

    <address class="address">
      PO BOX 418 Harbor Rd,<br>
      5th Avenue, Milton, USA
    </address>

    <div class="base-band"></div>
  </section>
</body>
</html>
```